Community Legal Website

The website is about a law in legal area (Fiscal), it has a moderator and the community also contributes with information.

Attention that this is not for a Law Firm. This is a community site where all the lawyers can contribute wiith their knowledge and at the same time where they can read the Official Law in the fiscal area.

The site is in portuguese, but we have attach information in english about the functionalities.

I attach information which represents the first version of the site done by html.. That is the site we intend to improve.

The site is quite simple because the main pages are:
- Home page;
- Section page (which has the Chapters and articles)
- Article page;

This pages all belong to the article:

redaccao_actual.htm, redaccoes_anteriores.htm, anotacoes.htm, jurisprudencia.htm, decisoesadministrativas.htm, minutas.htm, duvidas.htm

AS you see in all of them the options are always there.

The most important in this site is the usability of the content:

The FAQ, Contacts, Terms of conditions, who we are, are links less important.

Also there is a possibility to have in the homepage a higligh of certain articles that we want to raise from the others.

Please check the excel sheet as well as the zip file wich has the site in portuguese that you can use a website translator to check in your language.
Updates

We added a excel sheet with the functionalities in english which the site must have.

Reason: Because this is easter time we have increased the time for the deliver

Please check briefing update.

Reason: There were some request to extend the deadline because of the Easter

Hi!

Please read carefully the briefing. People are presenting me company web sites adn this is NOT a company web site. THis is a Site wich has a content of Laws. Please check the 1st version in the zip file and improve it. The options are there and you can translate in google tradutor or reading the excel sheet attach.

txs,
JV

Reason: My client need more desing choices

Target Market(s)

Lawyers, jurists and people related with the fiscal Law.

Industry/Entity Type

Legal

Requirements
Must have
• The interface should be clean and elegant.
It should also contribute to speed.
And try to avoid to many distract elements.
The site will be dinamic and with a backoffice, so in that you have to be carefully with the space dynamic. But you don't have to worry about the backoffice. Only the front office which is the public site.

```html
<!DOCTYPE html>
<html lang="pt">
<head>
<meta charset="utf-8">
<title>SOUSA VEIGA.net – Código do IRS, Artigo 32</title>
<link rel="stylesheet" href="https://fonts.googleapis.com/css2?family=Open+Sans:wght@400;600;700&display=swap">
<style>
:root{
  --teal:#557b73;
  --teal-dark:#466a62;
  --teal-text:#3f7a6d;
  --ink:#1d1d1d;
  --text:#333;
  --muted:#6a6a6a;
  --bar:#f3f3f3;
  --tab:#e4ebe9;
  --page-edge:#dedede;
  --footer:#e9e9e9;
}
*{box-sizing:border-box;margin:0;padding:0}
html,body{width:1200px;height:625px;overflow:hidden}
body{position:relative;background:#fff;font-family:"Open Sans",Arial,sans-serif;color:var(--text)}
.top-edge{position:absolute;left:0;top:0;width:1200px;height:5px;background:var(--page-edge)}
.brand{position:absolute;left:250px;top:64px;display:flex;align-items:center;gap:10px;font-size:14px;color:var(--ink);letter-spacing:.2px}
.brand-square{width:18px;height:18px;background:var(--teal)}
.main-nav{position:absolute;top:66px;left:560px;display:flex;font-size:11.5px;color:var(--ink)}
.main-nav a{color:inherit;text-decoration:none;position:relative;padding:0 12px}
.main-nav a.current{color:var(--teal-text)}
.nav-sep{position:absolute;top:-22px;width:14px;height:60px;transform:skewX(-18deg);background:linear-gradient(90deg,rgba(0,0,0,0) 0,rgba(0,0,0,.06) 100%)}
.article{position:absolute;left:233px;top:130px;width:735px;height:434px;background:#fff;box-shadow:-14px 0 14px -12px rgba(0,0,0,.18)}
.toolbar{position:absolute;left:0;width:735px;height:17px;background:var(--bar);display:flex;justify-content:flex-end;align-items:center;gap:16px;padding-right:14px;font-size:9.5px;color:var(--muted)}
.toolbar .code-menu{color:var(--teal-dark)}
.toolbar .ico{display:inline-block;width:6px;height:6px;border:1px solid #aaa;margin-left:3px;vertical-align:middle}
.toolbar-top{top:18px}
.toolbar-bottom{top:384px}
.header-band{position:absolute;left:0;top:35px;width:735px;height:55px;background:linear-gradient(90deg,var(--teal) 0,var(--teal) 85%,#6e948c 100%);color:#fff;text-align:center}
.header-band h1{font-size:16px;font-weight:700;margin-top:10px;letter-spacing:.2px}
.header-band p{font-size:11px;color:#b9d0ca;margin-top:1px}
.prev{position:absolute;left:42px;top:17px}
.next{position:absolute;right:28px;top:15px;display:flex;align-items:center;gap:8px;font-size:8.5px;line-height:10px;text-align:right}
.tabs{position:absolute;left:52px;top:92px;display:flex;font-size:8.5px;text-transform:uppercase;letter-spacing:.2px}
.tab{position:relative;height:21px;line-height:21px;padding:0 10px;margin-right:2px;color:var(--teal-text)}
.tab::before{content:"";position:absolute;inset:0;background:var(--tab);transform:skewX(-15deg);z-index:-1}
.tab.active{color:#fff;padding:0 12px 0 16px}
.tab.active::before{background:var(--teal-dark)}
.law-text{position:absolute;left:70px;top:134px;width:600px;font-size:8.6px;line-height:11px;color:#222}
.law-text h2{font-size:9px;font-weight:700;margin-bottom:10px}
.law-text p{margin-bottom:11px}
.site-footer{position:absolute;left:0;top:565px;width:1200px;height:60px;background:var(--footer);border-top:1px solid #dcdcdc;text-align:center;font-size:9.5px;color:#777;line-height:56px}
</style>
</head>
<body>
<div class="top-edge"></div>

<header>
  <div class="brand"><span class="brand-square"></span><span>SOUSA VEIGA.net</span></div>
  <nav class="main-nav">
    <a href="#">TERMOS DE UTILIZAÇÃO</a>
    <a href="#" class="current"><span class="nav-sep" style="left:-6px"></span>PERGUNTAS FREQUENTES<span class="nav-sep" style="right:-6px"></span></a>
    <a href="#">QUEM SOMOS</a>
  </nav>
</header>

<main class="article">
  <div class="toolbar toolbar-top">
    <span>Índice deste Código</span><span class="code-menu">Menu dos Códigos<span class="ico"></span></span><span>Gravar<span class="ico"></span></span><span>Imprimir<span class="ico"></span></span><span>Share +</span>
  </div>

  <div class="header-band">
    <svg class="prev" width="14" height="20" viewBox="0 0 14 20"><path d="M11 2 L3 10 L11 18" fill="none" stroke="#fff" stroke-width="3"/></svg>
    <h1>CÓDIGO DO IRS - Artigo 32</h1>
    <p>Encargos não dedutíveis para efeitos fiscais</p>
    <div class="next"><span>Artigo<br>seguinte</span><svg width="10" height="16" viewBox="0 0 10 16"><path d="M2 2 L8 8 L2 14" fill="none" stroke="#fff" stroke-width="2.5"/></svg></div>
  </div>

  <nav class="tabs">
    <span class="tab active">Redacção actual</span>
    <span class="tab">Redacções anteriores</span>
    <span class="tab">Anotações</span>
    <span class="tab">Jurisprudência</span>
    <span class="tab">Decisões administrativas</span>
    <span class="tab">Minutas</span>
    <span class="tab">Dúvidas</span>
  </nav>

  <article class="law-text">
    <h2>Em vigor desde 01-01-2012</h2>
    <p>1 - Para além das limitações previstas no Código do IRC, não são dedutíveis para efeitos de determinação do rendimento da categoria B, mesmo quando contabilizadas como custos ou perdas do exercício, as despesas de deslocações, viagens e estadas do sujeito passivo ou de membros do seu agregado familiar que com ele trabalham, na parte que exceder, no seu conjunto, 10% do total dos proveitos contabilizados, sujeitos e não isentos deste imposto. (Redacção da Lei n.º 109-B/2001, de 27 de Dezembro)</p>
    <p>2 - Por portaria do Ministro das Finanças podem ser fixados para efeitos do disposto neste artigo o número máximo de veículos e respectivo valor por sujeito passivo.</p>
    <p>3 - (Eliminado pela Lei n.º 109-B/2001, de 27 de Dezembro)</p>
    <p>4 - (Eliminado pela Lei n.º 109-B/2001, de 27 de Dezembro)</p>
    <p>5 - Quando o sujeito passivo afecte à sua actividade empresarial e profissional parte do imóvel destinado à sua habitação, os encargos dedutíveis com ela conexos referentes a amortizações ou rendas, energia, água e telefone fixo não podem ultrapassar 25% das respectivas despesas devidamente comprovadas.</p>
    <p>6 - Se o sujeito passivo exercer a sua actividade em conjunto com outros profissionais, os encargos dedutíveis são rateados em função da respectiva utilização ou, na falta de elementos que permitam o rateio, proporcionalmente aos rendimentos brutos auferidos.</p>
  </article>

  <div class="toolbar toolbar-bottom">
    <span>Índice deste Código</span><span class="code-menu">Menu dos Códigos<span class="ico"></span></span><span>Gravar<span class="ico"></span></span><span>Imprimir<span class="ico"></span></span><span>Share +</span>
  </div>
</main>

<footer class="site-footer">(c) SOUSA VEIGA - 2013</footer>
</body>
</html>
```